New company branded Power Point Template for presentations

We would like to have a clean and professional Slides app template made for our rebranding effort. It will be for our main company (Gordavexa) and will be used for both general introductory presentations and more technical industry related webinar and in-person presentations. We are a company in the manufacturing space working primarily in automotive. We provide simulation services to optimize production and softwares to allow users to do the same for themselves. The template needs to be easy to modify (even for novice users). I would like a good cover slide, content slides with common title / logo / etc. and a Q&A slide along with a final slide "Thank you" of similar. I have included our brand style guide in a high res pdf. Its images should be sufficient but please let me know if that is not the case.

```html
<!DOCTYPE html>
<html lang="en">
<head>
<meta charset="utf-8">
<title>Gordavexa presentation template</title>
<link href="https://fonts.googleapis.com/css2?family=Figtree:wght@400;600;700;800&display=swap" rel="stylesheet">
<style>
:root{
  --navy:#06365e;
  --teal:#1a9fb7;
  --orange:#f4a300;
  --paper:#ffffff;
  --mist:#f1f1f1;
  --line:#d9d9d9;
  --ink:#1b1b1b;
  --app-red:#c43e1c;
  --app-grey:#f3f3f3;
}
*{box-sizing:border-box;margin:0;padding:0}
html,body{width:1200px;height:1200px;overflow:hidden;background:#fff}
body{position:relative;font-family:'Figtree',sans-serif;color:var(--ink)}

.slide{position:absolute;width:264px;height:150px;background:var(--paper);overflow:hidden;box-shadow:0 0 3px rgba(0,0,0,.18)}
.slide .inner{position:absolute;left:9px;top:9px;right:9px;bottom:9px;background:var(--mist)}
.brand{position:absolute;display:flex;align-items:center;gap:2px;font-weight:700;color:var(--navy);letter-spacing:.04em}
.brand .dot{display:inline-block;background:var(--teal)}
.brand.mini{right:6px;top:6px;font-size:3.4px}
.brand.mini .dot{width:5px;height:5px}
.pg{position:absolute;right:2px;bottom:2px;width:6px;height:6px;background:var(--orange);color:#fff;font-size:3px;text-align:center;line-height:6px}
.h{position:absolute;font-weight:700;color:var(--navy);font-size:5px}
.h.light{color:#fff}
.h.teal{color:var(--teal)}
.p{font-size:2.6px;line-height:1.35;color:#333}
.p.light{color:#e7eef5}
.box{position:absolute}
.navy{background:var(--navy)}
ul.b{list-style:none}
ul.b li{font-size:2.6px;line-height:1.35;padding-left:4px;position:relative;margin-bottom:1.5px;color:#333}
ul.b li::before{content:"";position:absolute;left:0;top:1px;border-left:1px solid transparent;border-right:1px solid transparent;border-bottom:1.6px solid var(--orange)}
ul.b.light li{color:#e7eef5}

.headline{position:absolute;left:0;width:1200px;top:732px;text-align:center;font-size:24px;font-weight:800;color:#111}

.app{position:absolute;width:533px;height:300px;background:#e8e8e8;box-shadow:0 2px 8px rgba(0,0,0,.3);overflow:hidden}
.app .bar{height:11px;background:var(--app-red);display:flex;align-items:center;justify-content:center}
.app .bar span{width:100px;height:6px;background:#e07a5f;border-radius:1px}
.app .menu{height:8px;background:var(--app-grey);font-size:3.4px;display:flex;gap:7px;padding:2px 6px;color:#333}
.app .ribbon{height:30px;background:#fbfbfb;border-bottom:1px solid #ddd;position:relative}
.app .thumbs{position:absolute;left:6px;top:55px;width:68px;bottom:20px}
.app .thumb{width:62px;height:36px;background:#fff;border:1px solid #ccc;margin:0 0 5px 6px;position:relative}
.app .thumb.active{border:1.5px solid var(--app-red)}
.app .stage{position:absolute;left:86px;top:60px;right:16px;bottom:22px;background:#fff;box-shadow:0 0 2px rgba(0,0,0,.2)}
.app .task{position:absolute;left:0;right:0;bottom:0;height:12px;background:#1f1f1f}
.app .status{position:absolute;left:0;right:0;bottom:12px;height:6px;background:#f3f3f3;font-size:3px;padding-left:4px;color:#555}
.cover-title{position:absolute;font-weight:700;color:var(--navy)}
.cover-sub{position:absolute;color:var(--teal)}
.cover-rule{position:absolute;width:1px;background:var(--orange)}
.theme-chip{position:absolute;top:4px;width:24px;height:14px;border:1px solid #ccc;background:#fff}
.dialog{position:absolute;background:#f5f5f5;border:1px solid #aaa;box-shadow:0 2px 6px rgba(0,0,0,.3);font-size:3px;padding:3px}
.palette{position:absolute;background:#fff;border:1px solid #bbb;box-shadow:0 2px 5px rgba(0,0,0,.25);font-size:3px;padding:3px}
.sw{display:inline-block;width:5px;height:5px;margin-right:1px}
</style>
</head>
<body>

<!-- Row 1 -->
<section class="slide" style="left:50px;top:86px">
  <div class="brand" style="left:138px;top:24px;font-size:13px;gap:5px"><span class="dot" style="width:14px;height:14px"></span>GORDAVEXA</div>
  <div class="cover-rule" style="left:19px;top:103px;height:32px"></div>
  <div class="cover-title" style="left:27px;top:110px;font-size:11px">A Main Title Goes Here</div>
  <div class="cover-sub" style="left:27px;top:124px;font-size:4px">A small Title Goes Here</div>
</section>

<section class="slide" style="left:333px;top:86px">
  <div class="box" style="left:0;top:0;width:82px;height:150px;background:var(--mist)"></div>
  <div class="brand mini"><span class="dot"></span></div>
  <div class="h teal" style="left:24px;top:25px;font-size:5px">Lorem ipsum</div>
  <div class="box navy" style="left:22px;top:49px;width:78px;height:72px"></div>
  <div class="box" style="left:38px;top:49px;width:212px">
    <div style="display:flex;height:18px;align-items:center;border-bottom:.6px solid var(--orange)"><span class="p light" style="width:62px;text-align:right;font-weight:700;padding-right:5px">Lorem ipsum</span><span class="p" style="padding-left:6px">Lorem ipsum dolor sit amet, consectetuer adipiscing elit. Maecenas porttitor congue massa.</span></div>
    <div style="display:flex;height:18px;align-items:center;border-bottom:.6px solid var(--orange)"><span class="p light" style="width:62px;text-align:right;font-weight:700;padding-right:5px">Lorem ipsum</span><span class="p" style="padding-left:6px">Lorem ipsum dolor sit amet, consectetuer adipiscing elit.</span></div>
    <div style="display:flex;height:18px;align-items:center;border-bottom:.6px solid var(--orange)"><span class="p light" style="width:62px;text-align:right;font-weight:700;padding-right:5px">Lorem ipsum</span><span class="p" style="padding-left:6px">Lorem ipsum dolor sit amet, consectetuer adipiscing elit. Maecenas porttitor congue massa.</span></div>
    <div style="display:flex;height:18px;align-items:center"><span class="p light" style="width:62px;text-align:right;font-weight:700;padding-right:5px">Lorem ipsum</span><span class="p" style="padding-left:6px">Lorem ipsum dolor sit amet, consectetuer adipiscing elit. Maecenas porttitor congue massa.</span></div>
  </div>
  <div class="pg">2</div>
</section>

<section class="slide" style="left:617px;top:86px">
  <div class="inner"></div>
  <div class="brand mini"><span class="dot"></span></div>
  <div class="h" style="left:19px;top:28px">Lorem ipsum dolor</div>
  <div class="box p" style="left:24px;top:43px;font-weight:700">Lorem ipsum dolor sit amet, consectetuer</div>
  <div class="box" style="left:24px;top:52px;width:216px;height:13px" >
    <div class="navy" style="height:6px;display:flex;justify-content:space-around;font-size:2.4px;color:#fff;align-items:center"><span>Text here</span><span>Text here</span><span>Text here</span><span>Text here</span><span>Text here</span></div>
    <div style="height:13px;background:#dcdcdc;display:flex;justify-content:space-around;font-size:2.4px;color:#666"><span>Text here</span><span>Text here</span><span>Text here</span><span>Text here</span><span>Text here</span></div>
  </div>
  <div class="box p" style="left:22px;top:87px;width:220px"><b>Text here</b><br>Lorem ipsum dolor sit amet, consectetuer adipiscing elit. Maecenas porttitor congue massa.<br><b>Text here</b><br>Lorem ipsum dolor sit amet, consectetuer adipiscing elit. Maecenas porttitor congue massa.<br><b>Text here</b><br>Lorem ipsum dolor sit amet, consectetuer adipiscing elit. Maecenas porttitor congue massa.</div>
  <div class="pg">3</div>
</section>

<section class="slide" style="left:894px;top:86px">
  <div class="inner"></div>
  <div class="brand mini"><span class="dot"></span></div>
  <div class="h" style="left:19px;top:28px">Lorem ipsum</div>
  <div class="box p" style="left:19px;top:40px;width:72px">Lorem ipsum dolor sit amet, consectetuer adipiscing elit. Maecenas porttitor congue massa. Fusce posuere, magna sed pulvinar ultricies.<br><br>Lorem ipsum dolor sit amet, consectetuer adipiscing elit. Maecenas porttitor congue massa. Fusce posuere.<br><br>Lorem ipsum dolor sit amet, consectetuer adipiscing elit.</div>
  <div class="box navy" style="left:111px;top:24px;width:153px;height:64px;padding:5px 7px">
    <div style="font-size:4.5px;color:#fff;margin-bottom:5px">Lorem ipsum dolor sit amet</div>
    <ul class="b light"><li>Lorem ipsum dolor sit amet, consectetuer adipiscing elit. Maecenas porttitor congue massa. Fusce posuere.</li><li>Lorem ipsum dolor sit amet, consectetuer adipiscing elit. Maecenas porttitor congue massa. Fusce posuere.</li></ul>
  </div>
  <div class="h" style="left:118px;top:95px">Lorem ipsum dolor sit amet</div>
  <ul class="b box" style="left:118px;top:106px;width:130px"><li>Lorem ipsum dolor sit amet, consectetuer adipiscing elit. Maecenas porttitor congue massa. Fusce posuere.</li></ul>
  <div class="pg">4</div>
</section>

<!-- Row 2 -->
<section class="slide" style="left:56px;top:250px">
  <div class="inner"></div>
  <div class="brand mini"><span class="dot"></span></div>
  <div class="box navy" style="left:0;top:16px;width:109px;height:114px;padding:14px 18px">
    <div style="font-size:5.5px;font-weight:700;color:#fff;margin-bottom:10px">Lorem ipsum dolor sit amet</div>
    <div class="p light"><b>Lorem ipsum</b><br>Lorem ipsum dolor sit amet, consectetuer adipiscing elit. Maecenas porttitor congue massa.<br><br><b>Lorem ipsum</b><br>Lorem ipsum dolor sit amet, consectetuer adipiscing elit. Maecenas porttitor congue massa.<br><br><b>Lorem ipsum</b><br>Lorem ipsum dolor sit amet, consectetuer adipiscing elit.</div>
  </div>
  <div class="box" style="left:118px;top:30px;font-size:5px;color:var(--navy)">Lorem ipsum dolor<br>sit amet</div>
  <ul class="b box" style="left:118px;top:52px;width:124px"><li>Lorem ipsum dolor sit amet, consectetuer adipiscing elit.</li><li>Lorem ipsum dolor sit amet, consectetuer adipiscing elit.</li><li>Lorem ipsum dolor sit amet, consectetuer adipiscing elit.</li><li>Lorem ipsum dolor sit amet, consectetuer adipiscing elit.</li><li>Lorem ipsum dolor sit amet, consectetuer adipiscing elit.</li><li>Lorem ipsum dolor sit amet, consectetuer adipiscing elit.</li><li>Lorem ipsum dolor sit amet, consectetuer adipiscing elit.</li></ul>
  <div class="pg">5</div>
</section>

<section class="slide" style="left:333px;top:250px">
  <div class="box navy" style="left:9px;top:9px;right:9px;bottom:9px;padding:13px 16px">
    <div style="font-size:5px;color:#fff;margin-bottom:12px">Lorem ipsum dolor sit amet</div>
    <ul class="b light"><li>Lorem ipsum dolor sit amet, consectetuer adipiscing elit. Maecenas porttitor congue massa.</li><li>Lorem ipsum dolor sit amet, consectetuer adipiscing elit. Maecenas porttitor congue massa.</li><li>Lorem ipsum dolor sit amet, consectetuer adipiscing elit. Maecenas porttitor congue massa.</li><li>Lorem ipsum dolor sit amet, consectetuer adipiscing elit. Maecenas porttitor congue massa.</li><li>Lorem ipsum dolor sit amet, consectetuer adipiscing elit. Maecenas porttitor congue massa.</li><li>Lorem ipsum dolor sit amet, consectetuer adipiscing elit. Maecenas porttitor congue massa.</li><li>Lorem ipsum dolor sit amet, consectetuer adipiscing elit. Maecenas porttitor congue massa.</li></ul>
  </div>
  <div class="brand mini"><span class="dot"></span></div>
  <div class="pg">6</div>
</section>

<section class="slide" style="left:610px;top:250px">
  <div class="inner"></div>
  <div class="brand mini"><span class="dot"></span></div>
  <div class="box navy" style="left:17px;top:14px;width:229px;height:44px;padding:5px 7px">
    <div style="font-size:4.5px;color:#fff;margin-bottom:4px">Lorem ipsum dolor sit amet</div>
    <div style="display:grid;grid-template-columns:repeat(4,40px);padding-left:18px;gap:2px;font-size:2.6px;font-weight:700;color:#fff"><span>Lorem ipsum</span><span>Lorem ipsum</span><span>Lorem ipsum</span><span>Lorem ipsum</span><span>Lorem ipsum</span><span>Lorem ipsum</span><span>Lorem ipsum</span><span>Lorem ipsum</span><span>Lorem ipsum</span><span>Lorem ipsum</span><span>Lorem ipsum</span><span>Lorem ipsum</span></div>
  </div>
  <div class="h teal" style="left:18px;top:66px;font-size:4px">Lorem ipsum</div>
  <div class="box" style="left:18px;top:75px;width:103px"><div class="p"><b>Lorem ipsum:</b></div><ul class="b"><li>Lorem ipsum dolor sit amet, consectetuer adipiscing elit.</li><li>Lorem ipsum dolor sit amet, consectetuer adipiscing elit.</li><li>Lorem ipsum dolor sit amet, consectetuer adipiscing elit.</li></ul></div>
  <div class="h teal" style="left:124px;top:66px;font-size:4px">Lorem ipsum</div>
  <div class="box" style="left:124px;top:75px;width:118px"><div class="p"><b>Lorem ipsum:</b></div><ul class="b"><li>Lorem ipsum dolor sit amet, consectetuer adipiscing elit.</li><li>Lorem ipsum dolor sit amet, consectetuer adipiscing elit.</li><li>Lorem ipsum dolor sit amet, consectetuer adipiscing elit.</li><li>Lorem ipsum dolor sit amet, consectetuer adipiscing elit.</li></ul></div>
  <div class="pg">7</div>
</section>

<section class="slide" style="left:887px;top:250px">
  <div class="inner"></div>
  <div class="brand mini"><span class="dot"></span></div>
  <div class="h" style="left:18px;top:19px;font-size:4px">Lorem ipsu</div>
  <div class="box" style="left:18px;top:30px;width:128px"><div class="p"><b>Lorem ipsu</b><br>Lorem ipsum dolor sit amet, consectetuer adipiscing elit. Maecenas porttitor congue massa. Fusce posuere.</div><ul class="b"><li>Lorem ipsum dolor sit amet, consectetuer adipiscing elit.</li><li>Lorem ipsum dolor sit amet, consectetuer adipiscing elit. Maecenas porttitor congue massa.</li><li>Lorem ipsum dolor sit amet, consectetuer adipiscing elit.</li><li>Lorem ipsum dolor sit amet, consectetuer adipiscing elit. Maecenas porttitor congue massa.</li><li>Lorem ipsum dolor sit amet, consectetuer adipiscing elit.</li></ul></div>
  <div class="box navy" style="left:160px;top:22px;width:81px;height:107px;padding:10px 7px">
    <div style="font-size:4px;color:#fff;margin-bottom:6px">Lorem ipsum</div>
    <div class="p light"><b>Lorem ipsu:</b></div>
    <ul class="b light"><li>Lorem ipsum dolor sit amet, consectetuer adipiscing elit. Maecenas porttitor congue massa.</li><li>Lorem ipsum dolor sit amet, consectetuer adipiscing elit.</li></ul>
  </div>
  <div class="pg">8</div>
</section>

<!-- Row 3 -->
<section class="slide" style="left:56px;top:409px">
  <div class="inner"></div>
  <div class="brand mini"><span class="dot"></span></div>
  <div class="h" style="left:17px;top:20px;font-size:4px">Lorem ipsu</div>
  <div class="box" style="left:17px;top:31px;width:130px"><div class="p"><b>Lorem ipsu</b><br>Lorem ipsum dolor sit amet, consectetuer adipiscing elit. Maecenas porttitor congue massa.</div><ul class="b"><li>Lorem ipsum dolor sit amet, consectetuer adipiscing elit.</li><li>Lorem ipsum dolor sit amet, consectetuer adipiscing elit. Maecenas porttitor congue massa.</li><li>Lorem ipsum dolor sit amet, consectetuer adipiscing elit. Maecenas porttitor congue massa.</li><li>Lorem ipsum dolor sit amet, consectetuer adipiscing elit.</li><li>Lorem ipsum dolor sit amet, consectetuer adipiscing elit.</li></ul></div>
  <div class="box navy" style="left:160px;top:22px;width:80px;height:108px"></div>
  <div class="box" role="img" aria-label="Black and white mountain photograph" style="left:166px;top:27px;width:98px;height:103px;background:linear-gradient(160deg,#2a2a2a 0%,#0a0a0a 55%,#3a3a3a 75%,#111 100%)"></div>
  <div class="pg">9</div>
</section>

<section class="slide" style="left:333px;top:409px">
  <div class="inner"></div>
  <div class="brand mini"><span class="dot"></span></div>
  <div class="h" style="left:17px;top:20px;font-size:4px">Lorem ipsum dolor sit amet</div>
  <div class="box" style="left:17px;top:31px;width:150px"><div class="p"><b>Lorem ipsu</b><br>Lorem ipsum dolor sit amet, consectetuer adipiscing elit. Maecenas porttitor congue massa.</div><ul class="b"><li>Lorem ipsum dolor sit amet, consectetuer adipiscing elit.</li><li>Lorem ipsum dolor sit amet, consectetuer adipiscing elit. Maecenas porttitor.</li><li>Lorem ipsum dolor sit amet, consectetuer adipiscing elit.</li></ul></div>
  <div class="box navy" style="left:0;top:101px;width:174px;height:49px;padding:8px 17px">
    <div style="font-size:4px;font-weight:700;color:#fff;margin-bottom:4px">Lorem ipsum dolor sit amet</div>
    <div class="p light"><b>Lorem ipsu</b><br>Lorem ipsum dolor sit amet, consectetuer adipiscing elit. Maecenas porttitor congue massa. Fusce posuere.</div>
  </div>
  <div class="h" style="left:180px;top:25px;font-size:4px">Lorem ipsum</div>
  <div class="box" style="left:180px;top:37px;width:70px"><div class="p" style="color:var(--teal);font-weight:700">Lorem ipsum dolor :</div><ul class="b"><li>Lorem ipsum dolor sit amet</li><li>Lorem ipsum dolor sit amet</li><li>Lorem ipsum dolor sit amet</li><li>Lorem ipsum dolor sit amet</li><li>Lorem ipsum dolor sit amet</li><li>Lorem ipsum dolor sit amet</li><li>Lorem ipsum dolor sit amet</li><li>Lorem ipsum dolor sit amet</li><li>Lorem ipsum dolor sit amet</li><li>Lorem ipsum dolor sit amet</li></ul></div>
  <div class="pg">10</div>
</section>

<section class="slide" style="left:610px;top:409px">
  <div class="inner"></div>
  <div class="brand mini"><span class="dot"></span></div>
  <div class="box navy" style="left:9px;top:6px;width:120px;height:131px;padding:13px 8px">
    <div style="font-size:4px;font-weight:700;color:#fff;margin-bottom:12px">Lorem ipsum dolor sit amet</div>
    <div class="p light">Lorem ipsum dolor sit amet, consectetuer adipiscing elit. Maecenas porttitor congue massa.</div>
    <ul class="b light"><li>Lorem ipsum dolor sit amet, consectetuer adipiscing elit.</li><li>Lorem ipsum dolor sit amet, consectetuer adipiscing elit. Maecenas porttitor.</li><li>Lorem ipsum dolor sit amet, consectetuer adipiscing elit.</li></ul>
  </div>
  <div class="h" style="left:138px;top:19px;font-size:4px">Lorem ipsum dolor sit amet</div>
  <div class="box" style="left:138px;top:42px;width:110px"><div class="p">Lorem ipsum dolor sit amet, consectetuer adipiscing elit. Maecenas porttitor congue massa.</div><ul class="b"><li>Lorem ipsum dolor sit amet, consectetuer adipiscing elit.</li><li>Lorem ipsum dolor sit amet, consectetuer adipiscing elit. Maecenas porttitor.</li><li>Lorem ipsum dolor sit amet, consectetuer adipiscing elit.</li></ul></div>
  <div class="pg">11</div>
</section>

<section class="slide" style="left:887px;top:409px">
  <div class="inner"></div>
  <div class="brand mini"><span class="dot"></span></div>
  <div class="h" style="left:19px;top:27px;font-size:5px;font-weight:600;color:#111">Some Text</div>
  <div class="box" style="left:35px;top:48px;font-size:3px;font-weight:700;color:var(--navy);display:flex;gap:4px;align-items:center"><span style="width:6px;height:6px;background:var(--orange);color:#fff;text-align:center;line-height:6px">1</span>Lorem ipsum dolor sit amet, consectetuer adipiscing elit.</div>
  <div class="box p" style="left:52px;top:62px;width:190px">Lorem ipsum dolor sit amet, consectetuer adipiscing elit. Maecenas porttitor congue massa. Fusce posuere,<br><br>Lorem ipsum dolor sit amet, consectetuer adipiscing elit. Maecenas porttitor congue massa. Fusce posuere,<br><br>Lorem ipsum dolor sit amet, consectetuer adipiscing elit. Maecenas porttitor congue massa. Fusce posuere,<br><br>Lorem ipsum dolor sit amet, consectetuer adipiscing elit. Maecenas porttitor congue massa. Fusce posuere,</div>
  <div class="pg">12</div>
</section>

<!-- Row 4 -->
<section class="slide" style="left:337px;top:570px">
  <div class="box navy" style="left:9px;top:9px;right:9px;bottom:9px"></div>
  <div class="brand mini"><span class="dot"></span></div>
  <div class="h" style="left:19px;top:27px;font-size:5px;font-weight:600;color:var(--orange)">Some <span style="font-weight:400">Text</span></div>
  <div class="box" style="left:35px;top:53px;font-size:3px;font-weight:700;color:#fff;display:flex;gap:4px;align-items:center"><span style="width:6px;height:6px;background:#fff;color:var(--navy);text-align:center;line-height:6px">1</span>Lorem ipsum dolor sit amet, consectetuer adipiscing elit.</div>
  <div class="box p light" style="left:52px;top:66px;width:180px">Lorem ipsum dolor sit amet, consectetuer adipiscing elit. Maecenas porttitor congue massa. Fusce posuere,<br><br>Lorem ipsum dolor sit amet, consectetuer adipiscing elit. Maecenas porttitor congue massa. Fusce posuere,<br><br>Lorem ipsum dolor sit amet, consectetuer adipiscing elit. Maecenas porttitor congue massa. Fusce posuere,<br><br>Lorem ipsum dolor sit amet, consectetuer adipiscing elit. Maecenas porttitor congue massa. Fusce posuere,</div>
  <div class="pg">13</div>
</section>

<section class="slide" style="left:617px;top:570px">
  <div class="box navy" style="left:0;top:0;width:82px;height:150px"></div>
  <div class="brand" style="left:70px;top:65px;font-size:13px;gap:5px"><span class="dot" style="width:14px;height:14px"></span>GORDAVEXA</div>
</section>

<h2 class="headline">Custom brand colors and fonts added to the template</h2>

<!-- Application window: theme fonts -->
<section class="app" style="left:168px;top:786px">
  <div class="bar"><span></span></div>
  <div class="menu"><span>File</span><span>Home</span><span>Insert</span><span>Draw</span><span style="font-weight:700">Design</span><span>Transitions</span><span>Animations</span><span>Slide Show</span><span>Review</span><span>View</span></div>
  <div class="ribbon">
    <div class="theme-chip" style="left:6px"></div><div class="theme-chip" style="left:33px"></div><div class="theme-chip" style="left:60px;background:#eef5e0"></div><div class="theme-chip" style="left:87px;background:#f0e6e0"></div><div class="theme-chip" style="left:114px;background:#7ab"></div><div class="theme-chip" style="left:141px;background:#2f6b5b"></div><div class="theme-chip" style="left:168px;background:#4b2a5a"></div><div class="theme-chip" style="left:195px;background:#e8b04a"></div><div class="theme-chip" style="left:222px"></div><div class="theme-chip" style="left:249px;background:#3aa0d8"></div><div class="theme-chip" style="left:276px"></div><div class="theme-chip" style="left:303px;background:#d62b1f"></div><div class="theme-chip" style="left:330px;background:#5aa6e0"></div>
    <div class="theme-chip" style="left:355px"></div><div class="theme-chip" style="left:383px"></div><div class="theme-chip" style="left:411px;background:#000"></div><div class="theme-chip" style="left:439px;background:#000"></div>
  </div>
  <div class="thumbs">
    <div class="thumb active"><span class="brand" style="right:4px;top:5px;font-size:3px"><span class="dot" style="width:4px;height:4px"></span>GORDAVEXA</span></div>
    <div class="thumb"><div class="navy" style="position:absolute;left:6px;top:10px;width:20px;height:18px"></div></div>
    <div class="thumb" style="background:#f1f1f1"><div class="navy" style="position:absolute;left:8px;top:12px;width:45px;height:3px"></div></div>
    <div class="thumb" style="background:#f1f1f1"><div class="navy" style="position:absolute;right:4px;top:6px;width:30px;height:14px"></div></div>
    <div class="thumb"><div class="navy" style="position:absolute;left:0;top:4px;width:26px;height:28px"></div></div>
    <div class="thumb"><div class="navy" style="position:absolute;left:2px;top:2px;right:2px;bottom:2px"></div></div>
  </div>
  <div class="stage">
    <div class="cover-rule" style="left:28px;top:140px;height:52px"></div>
    <div class="cover-title" style="left:38px;top:152px;font-size:17px">A Main Title Goes Here</div>
    <div class="cover-sub" style="left:38px;top:174px;font-size:6px">A small Title Goes Here</div>
  </div>
  <div class="dialog" style="left:204px;top:117px;width:124px;height:52px">
    <div style="margin-bottom:4px">Edit Theme Fonts</div>
    <div>Heading font: <span style="background:#fff;border:1px solid #bbb;padding:0 20px 0 2px">Geist</span></div>
    <div style="margin-top:2px">Body font: <span style="background:#fff;border:1px solid #bbb;padding:0 12px 0 2px">Figtree</span></div>
    <div style="margin-top:2px">Name: <span style="background:#fff;border:1px solid #bbb;padding:0 40px 0 2px">Gordavexa</span></div>
    <div style="position:absolute;right:4px;bottom:3px;display:flex;gap:3px"><span style="border:1px solid #3a7bd5;padding:0 6px;background:#fff">Save</span><span style="border:1px solid #bbb;padding:0 5px;background:#fff">Cancel</span></div>
  </div>
  <div class="status">Slide 1 of 14</div>
  <div class="task"></div>
</section>

<!-- Application window: theme colours -->
<section class="app" style="left:531px;top:862px">
  <div class="bar"><span></span></div>
  <div class="menu"><span>File</span><span style="font-weight:700">Home</span><span>Insert</span><span>Draw</span><span>Design</span><span>Transitions</span><span>Animations</span><span>Slide Show</span><span>Review</span><span>View</span></div>
  <div class="ribbon"></div>
  <div class="thumbs">
    <div class="thumb active"><span class="brand" style="right:4px;top:5px;font-size:3px"><span class="dot" style="width:4px;height:4px"></span>GORDAVEXA</span></div>
    <div class="thumb"><div class="navy" style="position:absolute;left:6px;top:10px;width:20px;height:18px"></div></div>
    <div class="thumb" style="background:#f1f1f1"><div class="navy" style="position:absolute;left:8px;top:12px;width:45px;height:3px"></div></div>
    <div class="thumb" style="background:#f1f1f1"><div class="navy" style="position:absolute;right:4px;top:6px;width:30px;height:14px"></div></div>
    <div class="thumb"><div class="navy" style="position:absolute;left:0;top:4px;width:26px;height:28px"></div></div>
    <div class="thumb"><div class="navy" style="position:absolute;left:2px;top:2px;right:2px;bottom:2px"></div></div>
  </div>
  <div class="stage">
    <div class="brand" style="left:170px;top:30px;font-size:20px;gap:7px"><span class="dot" style="width:22px;height:22px"></span>GORDAVEXA</div>
    <div class="cover-rule" style="left:28px;top:145px;height:52px"></div>
    <div class="cover-title" style="left:38px;top:158px;font-size:17px">A Main Title Goes Here</div>
    <div class="cover-sub" style="left:38px;top:180px;font-size:6px">A small Title Goes Here</div>
  </div>
  <div class="palette" style="left:352px;top:22px;width:78px;height:168px">
    <div>Theme Colors</div>
    <div style="margin:2px 0"><span class="sw" style="background:#fff;border:.5px solid #ccc"></span><span class="sw" style="background:#000"></span><span class="sw" style="background:#e7e6e6"></span><span class="sw" style="background:#44546a"></span><span class="sw" style="background:#06365e"></span><span class="sw" style="background:#1a9fb7"></span><span class="sw" style="background:#2aa6d8"></span><span class="sw" style="background:#f4a300"></span><span class="sw" style="background:#a5a5a5"></span><span class="sw" style="background:#666"></span></div>
    <div style="height:36px;background:linear-gradient(90deg,#ddd,#333 20%,#6a8 40%,#1a9fb7 55%,#f4a300 75%,#999);opacity:.7;margin-bottom:5px"></div>
    <div>Standard Colors</div>
    <div style="margin:2px 0 4px"><span class="sw" style="background:#c00000"></span><span class="sw" style="background:#f00"></span><span class="sw" style="background:#ffc000"></span><span class="sw" style="background:#ff0"></span><span class="sw" style="background:#92d050"></span><span class="sw" style="background:#00b050"></span><span class="sw" style="background:#00b0f0"></span><span class="sw" style="background:#0070c0"></span><span class="sw" style="background:#002060"></span><span class="sw" style="background:#7030a0"></span></div>
    <div>Recent Colors</div>
    <div style="margin:2px 0 6px"><span class="sw" style="background:#e8562a"></span><span class="sw" style="background:#06365e"></span><span class="sw" style="background:#6d8cb4"></span><span class="sw" style="background:#777"></span><span class="sw" style="background:#1a9fb7"></span><span class="sw" style="background:#7fd8ec"></span></div>
    <div style="line-height:2.6">No Fill<br>More Fill Colors…<br>Eyedropper<br>Picture…<br>Gradient<br>Texture</div>
  </div>
  <div class="status">Slide 1 of 14</div>
  <div class="task"></div>
</section>

</body>
</html>
```